We are looking to create a graphic that will be used in Facebook posts each week to show the daily Porchlight Report. Attached is an example of what we are looking for. We need to be able to update the forecast. So we will need hi-res vector files. The graphics need to represent the level of mosquito activity: SLIGHT, AVERAGE, INTENSE, EXTREME

```html
<!DOCTYPE html>
<html lang="en">
<head>
<meta charset="utf-8">
<title>Porchlight Report – Weekly Activity Layouts</title>
<link href="https://fonts.googleapis.com/css2?family=Mulish:wght@600;700&display=swap" rel="stylesheet">
<style>
  :root{
    --ink:#111;
    --white:#fff;
    --grey-panel:#e8e8e8;
    --grey-head:#d0d0d0;
    --grey-rule:#7a7a7a;
    --blue-band:#dff0fb;
    --blue-rule:#a9d6f2;
    --tile-light:#e6e6e6;
    --tile-dark:#bfbfbf;
    --ring:#d4d4d4;
    --green:#8cc63f;
    --orange:#f7a21b;
    --red:#e3131b;
    --maroon:#7a1410;
  }
  *{box-sizing:border-box;margin:0;padding:0}
  html,body{width:849px;height:1200px;overflow:hidden;background:var(--white)}
  body{position:relative;font-family:"Mulish",sans-serif;color:var(--ink)}
  .option-title{position:absolute;left:33px;font-size:16px;font-weight:700}
  .week{position:absolute;display:grid;grid-template-columns:repeat(7,1fr);overflow:hidden}
  .day{position:relative;display:flex;flex-direction:column;align-items:center}
  .day-name{font-size:16px;font-weight:600;letter-spacing:.3px}
  .day-date{font-size:16px;font-weight:600;margin-top:9px;letter-spacing:1px}
  .level{font-size:13px;font-weight:700;letter-spacing:.2px}
  .gauge{width:78px;height:78px;display:block}

  /* Option 1 */
  .week--header{left:60px;top:56px;width:739px;height:233px;background:var(--grey-panel);border-radius:10px;
    background-image:linear-gradient(var(--grey-head) 0 86px,transparent 86px)}
  .week--header .day{padding-top:22px}
  .week--header .day+.day::before{content:"";position:absolute;left:0;top:27px;bottom:20px;width:1px;background:var(--grey-rule)}
  .week--header .gauge{margin-top:34px}
  .week--header .level{margin-top:12px}

  /* Option 2 */
  .week--stripes{left:60px;top:353px;width:733px;height:235px;border-radius:8px}
  .week--stripes .day{padding-top:26px}
  .week--stripes .day:nth-child(odd){background:var(--blue-band)}
  .week--stripes::after{content:"";position:absolute;left:0;right:0;top:92px;height:1px;background:var(--blue-rule)}
  .week--stripes .gauge{margin-top:30px}
  .week--stripes .level{margin-top:12px}

  /* Option 3 */
  .week--dark{left:60px;top:632px;width:728px;height:251px;border-radius:8px;
    background:linear-gradient(#000 0%,#1a1a1a 18%,#8a8a8a 62%,#e8e8e8 100%)}
  .week--dark .day{padding-top:34px}
  .week--dark .day+.day::before{content:"";position:absolute;left:0;top:32px;bottom:30px;width:1px;
    background:linear-gradient(rgba(255,255,255,.25),rgba(255,255,255,.15))}
  .week--dark .day-name,.week--dark .day-date{color:var(--white)}
  .week--dark .gauge{margin-top:34px}
  .week--dark .level{margin-top:12px}

  /* Option 4 */
  .week--tiles{left:62px;top:937px;width:722px;height:230px;column-gap:5px;grid-template-rows:147px 78px;row-gap:5px;background:var(--white)}
  .tile{display:flex;flex-direction:column;align-items:center;background:var(--tile-light)}
  .tile.is-dark{background:var(--tile-dark)}
  .tile--gauge{padding-top:19px}
  .tile--gauge .level{margin-top:10px}
  .tile--date{padding-top:15px}
  .tile--date .day-date{margin-top:7px}
</style>
</head>
<body>

<svg width="0" height="0" style="position:absolute" aria-hidden="true">
  <defs>
    <g id="dial-base">
      <circle cx="40" cy="40" r="39" fill="var(--white)"/>
      <circle cx="40" cy="40" r="32" fill="none" stroke="var(--ring)" stroke-width="9"/>
    </g>
    <g id="arc-green"><circle cx="40" cy="40" r="32" fill="none" stroke="var(--green)" stroke-width="9" pathLength="100" stroke-dasharray="25 100" transform="rotate(90 40 40)"/></g>
    <g id="arc-orange"><circle cx="40" cy="40" r="32" fill="none" stroke="var(--orange)" stroke-width="9" pathLength="100" stroke-dasharray="25 100" stroke-dashoffset="-25" transform="rotate(90 40 40)"/></g>
    <g id="arc-red"><circle cx="40" cy="40" r="32" fill="none" stroke="var(--red)" stroke-width="9" pathLength="100" stroke-dasharray="22 100" stroke-dashoffset="-50" transform="rotate(90 40 40)"/></g>
    <g id="arc-maroon"><circle cx="40" cy="40" r="32" fill="none" stroke="var(--maroon)" stroke-width="9" pathLength="100" stroke-dasharray="28 100" stroke-dashoffset="-72" transform="rotate(90 40 40)"/></g>

    <g id="gauge-slight"><use href="#dial-base"/><use href="#arc-green"/><circle cx="40" cy="40" r="15" fill="var(--green)" opacity=".85"/></g>
    <g id="gauge-average"><use href="#dial-base"/><use href="#arc-green"/><use href="#arc-orange"/><circle cx="40" cy="40" r="15" fill="var(--orange)" opacity=".85"/></g>
    <g id="gauge-intense"><use href="#dial-base"/><use href="#arc-green"/><use href="#arc-orange"/><use href="#arc-red"/><circle cx="40" cy="40" r="15" fill="var(--red)" opacity=".85"/></g>
    <g id="gauge-extreme"><use href="#dial-base"/><use href="#arc-green"/><use href="#arc-orange"/><use href="#arc-red"/><use href="#arc-maroon"/><circle cx="40" cy="40" r="15" fill="var(--maroon)" opacity=".9"/></g>
  </defs>
</svg>

<h2 class="option-title" style="top:20px">Option 1</h2>
<section class="week week--header">
  <div class="day"><span class="day-name">SUN</span><span class="day-date">?/?</span><svg class="gauge" viewBox="0 0 80 80" role="img" aria-label="Green mosquito icon, slight activity"><use href="#gauge-slight"/></svg><span class="level">SLIGHT</span></div>
  <div class="day"><span class="day-name">MON</span><span class="day-date">?/?</span><svg class="gauge" viewBox="0 0 80 80" role="img" aria-label="Green mosquito icon, slight activity"><use href="#gauge-slight"/></svg><span class="level">SLIGHT</span></div>
  <div class="day"><span class="day-name">TUE</span><span class="day-date">?/?</span><svg class="gauge" viewBox="0 0 80 80" role="img" aria-label="Red mosquito icon, intense activity"><use href="#gauge-intense"/></svg><span class="level">INTENCE</span></div>
  <div class="day"><span class="day-name">WED</span><span class="day-date">?/?</span><svg class="gauge" viewBox="0 0 80 80" role="img" aria-label="Dark red mosquito icon, extreme activity"><use href="#gauge-extreme"/></svg><span class="level">EXTREME</span></div>
  <div class="day"><span class="day-name">THU</span><span class="day-date">?/?</span><svg class="gauge" viewBox="0 0 80 80" role="img" aria-label="Red mosquito icon, intense activity"><use href="#gauge-intense"/></svg><span class="level">INTENCE</span></div>
  <div class="day"><span class="day-name">FRI</span><span class="day-date">?/?</span><svg class="gauge" viewBox="0 0 80 80" role="img" aria-label="Orange mosquito icon, average activity"><use href="#gauge-average"/></svg><span class="level">AVERAGE</span></div>
  <div class="day"><span class="day-name">SAT</span><span class="day-date">?/?</span><svg class="gauge" viewBox="0 0 80 80" role="img" aria-label="Red mosquito icon, intense activity"><use href="#gauge-intense"/></svg><span class="level">INTENCE</span></div>
</section>

<h2 class="option-title" style="top:312px">Option 2</h2>
<section class="week week--stripes">
  <div class="day"><span class="day-name">SUN</span><span class="day-date">?/?</span><svg class="gauge" viewBox="0 0 80 80" role="img" aria-label="Green mosquito icon, slight activity"><use href="#gauge-slight"/></svg><span class="level">SLIGHT</span></div>
  <div class="day"><span class="day-name">MON</span><span class="day-date">?/?</span><svg class="gauge" viewBox="0 0 80 80" role="img" aria-label="Green mosquito icon, slight activity"><use href="#gauge-slight"/></svg><span class="level">SLIGHT</span></div>
  <div class="day"><span class="day-name">TUE</span><span class="day-date">?/?</span><svg class="gauge" viewBox="0 0 80 80" role="img" aria-label="Red mosquito icon, intense activity"><use href="#gauge-intense"/></svg><span class="level">INTENCE</span></div>
  <div class="day"><span class="day-name">WED</span><span class="day-date">?/?</span><svg class="gauge" viewBox="0 0 80 80" role="img" aria-label="Dark red mosquito icon, extreme activity"><use href="#gauge-extreme"/></svg><span class="level">EXTREME</span></div>
  <div class="day"><span class="day-name">THU</span><span class="day-date">?/?</span><svg class="gauge" viewBox="0 0 80 80" role="img" aria-label="Red mosquito icon, intense activity"><use href="#gauge-intense"/></svg><span class="level">INTENCE</span></div>
  <div class="day"><span class="day-name">FRI</span><span class="day-date">?/?</span><svg class="gauge" viewBox="0 0 80 80" role="img" aria-label="Orange mosquito icon, average activity"><use href="#gauge-average"/></svg><span class="level">AVERAGE</span></div>
  <div class="day"><span class="day-name">SAT</span><span class="day-date">?/?</span><svg class="gauge" viewBox="0 0 80 80" role="img" aria-label="Red mosquito icon, intense activity"><use href="#gauge-intense"/></svg><span class="level">INTENCE</span></div>
</section>

<h2 class="option-title" style="top:602px">Option 3</h2>
<section class="week week--dark">
  <div class="day"><span class="day-name">SUN</span><span class="day-date">?/?</span><svg class="gauge" viewBox="0 0 80 80" role="img" aria-label="Green mosquito icon, slight activity"><use href="#gauge-slight"/></svg><span class="level">SLIGHT</span></div>
  <div class="day"><span class="day-name">MON</span><span class="day-date">?/?</span><svg class="gauge" viewBox="0 0 80 80" role="img" aria-label="Green mosquito icon, slight activity"><use href="#gauge-slight"/></svg><span class="level">SLIGHT</span></div>
  <div class="day"><span class="day-name">TUE</span><span class="day-date">?/?</span><svg class="gauge" viewBox="0 0 80 80" role="img" aria-label="Red mosquito icon, intense activity"><use href="#gauge-intense"/></svg><span class="level">INTENCE</span></div>
  <div class="day"><span class="day-name">WED</span><span class="day-date">?/?</span><svg class="gauge" viewBox="0 0 80 80" role="img" aria-label="Dark red mosquito icon, extreme activity"><use href="#gauge-extreme"/></svg><span class="level">EXTREME</span></div>
  <div class="day"><span class="day-name">THU</span><span class="day-date">?/?</span><svg class="gauge" viewBox="0 0 80 80" role="img" aria-label="Red mosquito icon, intense activity"><use href="#gauge-intense"/></svg><span class="level">INTENCE</span></div>
  <div class="day"><span class="day-name">FRI</span><span class="day-date">?/?</span><svg class="gauge" viewBox="0 0 80 80" role="img" aria-label="Orange mosquito icon, average activity"><use href="#gauge-average"/></svg><span class="level">AVERAGE</span></div>
  <div class="day"><span class="day-name">SAT</span><span class="day-date">?/?</span><svg class="gauge" viewBox="0 0 80 80" role="img" aria-label="Red mosquito icon, intense activity"><use href="#gauge-intense"/></svg><span class="level">INTENCE</span></div>
</section>

<h2 class="option-title" style="top:900px">Option 4</h2>
<section class="week week--tiles">
  <div class="tile tile--gauge"><svg class="gauge" viewBox="0 0 80 80" role="img" aria-label="Green mosquito icon, slight activity"><use href="#gauge-slight"/></svg><span class="level">SLIGHT</span></div>
  <div class="tile tile--gauge is-dark"><svg class="gauge" viewBox="0 0 80 80" role="img" aria-label="Green mosquito icon, slight activity"><use href="#gauge-slight"/></svg><span class="level">SLIGHT</span></div>
  <div class="tile tile--gauge"><svg class="gauge" viewBox="0 0 80 80" role="img" aria-label="Red mosquito icon, intense activity"><use href="#gauge-intense"/></svg><span class="level">INTENCE</span></div>
  <div class="tile tile--gauge is-dark"><svg class="gauge" viewBox="0 0 80 80" role="img" aria-label="Dark red mosquito icon, extreme activity"><use href="#gauge-extreme"/></svg><span class="level">EXTREME</span></div>
  <div class="tile tile--gauge"><svg class="gauge" viewBox="0 0 80 80" role="img" aria-label="Red mosquito icon, intense activity"><use href="#gauge-intense"/></svg><span class="level">INTENCE</span></div>
  <div class="tile tile--gauge is-dark"><svg class="gauge" viewBox="0 0 80 80" role="img" aria-label="Orange mosquito icon, average activity"><use href="#gauge-average"/></svg><span class="level">AVERAGE</span></div>
  <div class="tile tile--gauge"><svg class="gauge" viewBox="0 0 80 80" role="img" aria-label="Red mosquito icon, intense activity"><use href="#gauge-intense"/></svg><span class="level">INTENCE</span></div>

  <div class="tile tile--date"><span class="day-name">SUN</span><span class="day-date">?/?</span></div>
  <div class="tile tile--date is-dark"><span class="day-name">MON</span><span class="day-date">?/?</span></div>
  <div class="tile tile--date"><span class="day-name">TUE</span><span class="day-date">?/?</span></div>
  <div class="tile tile--date is-dark"><span class="day-name">WED</span><span class="day-date">?/?</span></div>
  <div class="tile tile--date"><span class="day-name">THU</span><span class="day-date">?/?</span></div>
  <div class="tile tile--date is-dark"><span class="day-name">FRI</span><span class="day-date">?/?</span></div>
  <div class="tile tile--date"><span class="day-name">SAT</span><span class="day-date">?/?</span></div>
</section>

</body>
</html>
```